Postcard Design for Direct Mail Campaign for PIttsburgh area attorney

I am an attorney in Pittsburgh, I did this before and selected three designs. I am not sure if those responding can see which three I selected. Those designs are in use now. All 3 go out. The issue is they cost the standard mailing rate and I will use all 3 of those forever. There will be times I would like to take advantage of the postcard mailing rate and thus this one is smaller. I want the postcard to emphasize I do criminal and SOME civil law. See my sites www.larvendefensecounsel.com and www.tobquill.net.

IN FACT I AM PUTTING THE THREE I AM MAILING RIGHT NOW IN THE IMAGES> I TRUST THAT THESE WILL BE USED TO INSPIRE AND GUIDE AND NO COPY. i Cannot upload those images. You can probably see my 3 winners.

Target Market(s)

Pittsburgh area people who may need a criminal attorney or a civil attorney.

Industry/Entity Type

Legal

Colors
ec1f27

Requirements
Must have
• A balanced criminal - civil thing as these are going to people in the mail with no envelope.
Nice to have
• On my site www.larvendefensecounsel.com I have badges in the sidebar.
Should not have
• People being arrested. I am putting up new images.

```html
<!DOCTYPE html>
<html lang="en">
<head>
<meta charset="utf-8">
<title>Daniel R. Halvorsen – Postcard</title>
<link rel="stylesheet" href="https://fonts.googleapis.com/css2?family=Marcellus&family=Oswald:wght@500;600&family=Open+Sans:ital,wght@0,400;0,600;1,400&display=swap">
<style>
  :root {
    --stage-light: #cfd0d2;
    --stage-dark: #b7b8bb;
    --maroon: #5a0606;
    --maroon-deep: #3a0000;
    --maroon-back: #520000;
    --charcoal: #23272a;
    --gold: #f4c44a;
    --gold-deep: #c8901e;
    --red: #ec1f27;
    --white: #ffffff;
    --panel: #ebebeb;
    --ink: #2a2a2a;
  }
  * { box-sizing: border-box; margin: 0; padding: 0; }
  html, body { width: 1200px; height: 1200px; overflow: hidden; }
  body { position: relative; background: var(--stage-light); font-family: "Open Sans", sans-serif; }
  .stage-shapes { position: absolute; inset: 0; }

  .card { position: absolute; left: 240px; width: 710px; overflow: hidden; }
  .card-front { top: 74px; height: 476px; background: linear-gradient(135deg, #4a0303 0%, var(--maroon) 45%, #6a0a0a 100%); }
  .card-back { top: 634px; height: 482px; background: var(--white); border: 1px solid #333; }

  .front-shapes { position: absolute; inset: 0; }
  .firm-title { position: absolute; left: 40px; top: 24px; width: 330px; text-align: center; font-family: "Marcellus", serif; font-weight: 400; color: var(--white); font-size: 26px; line-height: 32px; letter-spacing: .5px; }
  .firm-subtitle { position: absolute; left: 24px; top: 91px; font-family: "Marcellus", serif; color: #e9e2d2; font-size: 11.5px; letter-spacing: .3px; }
  .need-attorney { position: absolute; right: 26px; top: 20px; font-family: "Oswald", sans-serif; font-weight: 600; color: var(--white); font-size: 17px; }
  .call-bar { position: absolute; left: 494px; top: 42px; right: 0; height: 31px; background: var(--red); font-family: "Oswald", sans-serif; font-weight: 600; color: var(--white); font-size: 23px; line-height: 31px; padding-left: 10px; }
  .web-links { position: absolute; right: 26px; top: 95px; text-align: right; font-family: "Oswald", sans-serif; font-weight: 500; color: var(--gold); font-size: 14px; line-height: 19px; }

  .services { position: absolute; left: 22px; top: 149px; color: var(--white); }
  .point { font-family: "Open Sans", sans-serif; font-weight: 600; color: var(--gold); font-size: 13.4px; line-height: 18px; padding-left: 18px; position: relative; }
  .point::before { content: ""; position: absolute; left: 0; top: 4px; width: 10px; height: 10px; background: var(--gold); clip-path: polygon(25% 0, 75% 0, 100% 50%, 75% 100%, 25% 100%, 0 50%); }
  .practice-list { list-style: none; margin: 3px 0 4px 32px; font-size: 12px; line-height: 17.4px; color: var(--white); text-transform: uppercase; }
  .points-more .point { margin-top: 5px; }
  .appeals { list-style: none; margin: 6px 0 0 32px; font-size: 11.6px; line-height: 19.2px; color: var(--white); }
  .appeals li { position: relative; padding-left: 12px; }
  .appeals li::before { content: ""; position: absolute; left: 0; top: 8px; width: 4px; height: 4px; border-radius: 50%; background: var(--white); }

  .experience-seal { position: absolute; left: 392px; top: 146px; width: 118px; height: 118px; border-radius: 50%; background: radial-gradient(circle, var(--gold) 0%, var(--gold-deep) 100%); }
  .photo-tiles { position: absolute; left: 444px; top: 140px; width: 262px; height: 266px; }

  .back-left { position: absolute; left: 0; top: 0; width: 394px; height: 100%; background: var(--maroon-back); }
  .badge-panel { position: absolute; left: 22px; top: 24px; width: 362px; height: 170px; background: var(--panel); }
  .badge-panel svg { width: 100%; height: 100%; }
  .tagline { position: absolute; left: 22px; top: 194px; width: 178px; height: 108px; background: var(--maroon-deep); color: var(--white); font-style: italic; font-size: 12.6px; line-height: 17px; padding: 9px 6px 0 6px; text-align: justify; hyphens: auto; }
  .office-photo { position: absolute; left: 200px; top: 194px; width: 184px; height: 108px; background: linear-gradient(135deg, #8a8a8a, #2d2d2d 60%, #5a5a5a); }
  .consultation { position: absolute; left: 0; top: 322px; width: 394px; text-align: center; color: var(--white); }
  .consultation .label { font-size: 18px; line-height: 24px; letter-spacing: .3px; }
  .consultation .phone { font-size: 22px; line-height: 27px; }
  .consultation .phone small { font-size: 18px; }
  .consultation .email { font-size: 16.5px; line-height: 27px; }

  .mail-address { position: absolute; left: 402px; top: 24px; font-style: normal; font-size: 13.5px; line-height: 21.6px; color: var(--ink); text-transform: uppercase; }
  .mail-address .addressee { font-size: 15px; }
  .stamp-box { position: absolute; left: 578px; top: 35px; width: 112px; height: 76px; border: 2px solid #111; font-size: 16px; line-height: 72px; text-align: center; color: #111; }
</style>
</head>
<body>
  <svg class="stage-shapes" viewBox="0 0 1200 1200" aria-hidden="true">
    <polygon points="0,0 420,0 1200,760 1200,1200 960,1200 0,250" fill="var(--stage-dark)"/>
    <polygon points="0,250 960,1200 0,1200" fill="#c4c5c7"/>
  </svg>

  <section class="card card-front">
    <svg class="front-shapes" viewBox="0 0 710 476" aria-hidden="true">
      <polygon points="240,476 560,150 710,300 710,476" fill="#4c0303" opacity=".55"/>
      <polygon points="0,0 710,0 710,79 440,79 412,106 0,106" fill="var(--charcoal)"/>
      <polygon points="0,106 412,106 440,79 710,79 710,85 443,85 415,113 0,113" fill="var(--gold-deep)"/>
    </svg>

    <h1 class="firm-title">THE LAW OFFICE OF<br>DANIEL R. HALVORSEN</h1>
    <p class="firm-subtitle">PITTSBURGH CRIMINAL DEFENSE-PERSONAL INJURY ATTORNEY</p>
    <p class="need-attorney">NEED AN ATTORNEY?</p>
    <p class="call-bar">CALL 412-555-0148</p>
    <p class="web-links">VISIT: WWW.TOBQUILL.NET<br>WWW.LARVENDEFENSECOUNSEL.COM</p>

    <div class="services">
      <p class="point">25 YEARS’ EXPERIENCE ON</p>
      <ul class="practice-list">
        <li>DUI Defence</li>
        <li>Personal Injury</li>
        <li>Criminal Defence</li>
        <li>Traffic Citations/ License Issues</li>
        <li>Appeals/ Post-Conviction</li>
      </ul>
      <div class="points-more">
        <p class="point">REASONABLE FEES IN BOTH CRIMINAL AND CIVIL CASES</p>
        <p class="point">EXTENSIVE EXPERIENCE WITH A PROVEN RECORD OF SUCCESS</p>
        <p class="point">SOME OF HIS NOTABLE APPEALS</p>
      </div>
      <ul class="appeals">
        <li>United States v. Calloway, 281 F.3d 412 (3rd Cir. 2002)</li>
        <li>Commonwealth v. Brandt , 931 A.2d 264 (Pa.Super. 2007)</li>
        <li>Commonwealth v. Pryor, 912 A.2d 817 (Pa.Super 2006)</li>
        <li>Kessler v. Pennsylvania Board of Probation and Parole ,761 A.2d 443 (Pa.Cmwlth 2000)</li>
        <li>Commonwealth v. Kessler, 714 A.2d 1209 (Pa.Super. 1997)</li>
        <li>Commonwealth v. Dorsey, 548 Pa. 471, 684 A.2d 1279 (1995)</li>
        <li>Commonwealth v. Alvarado, 541 Pa. 8, 676 A.2d 752 (1993)</li>
      </ul>
    </div>

    <svg class="photo-tiles" viewBox="0 0 262 266" role="img" aria-label="Four diamond photo tiles: scales of justice and gavel, an officer writing a ticket, an attorney at his desk, a damaged car">
      <defs>
        <linearGradient id="tileWarm" x1="0" y1="0" x2="1" y2="1"><stop offset="0" stop-color="#e8d2b0"/><stop offset="1" stop-color="#6b4520"/></linearGradient>
        <linearGradient id="tileBlue" x1="0" y1="0" x2="1" y2="1"><stop offset="0" stop-color="#4a5f7a"/><stop offset="1" stop-color="#1c2330"/></linearGradient>
        <linearGradient id="tileOffice" x1="0" y1="0" x2="1" y2="1"><stop offset="0" stop-color="#c9d3de"/><stop offset="1" stop-color="#55677a"/></linearGradient>
        <linearGradient id="tileSteel" x1="0" y1="0" x2="1" y2="1"><stop offset="0" stop-color="#e3e6ea"/><stop offset="1" stop-color="#6e767e"/></linearGradient>
      </defs>
      <g stroke="var(--white)" stroke-width="5" stroke-linejoin="miter">
        <polygon points="130,6 192,68 130,130 68,68" fill="url(#tileWarm)"/>
        <polygon points="64,72 126,134 64,196 2,134" fill="url(#tileBlue)"/>
        <polygon points="196,72 258,134 196,196 134,134" fill="url(#tileOffice)"/>
        <polygon points="130,138 192,200 130,262 68,200" fill="url(#tileSteel)"/>
      </g>
    </svg>

    <div class="experience-seal" role="img" aria-label="Gold seal reading Experience 25 Years"></div>
  </section>

  <section class="card card-back">
    <div class="back-left">
      <div class="badge-panel">
        <svg viewBox="0 0 362 170" role="img" aria-label="Award and membership badges">
          <rect x="6" y="22" width="72" height="26" rx="3" fill="#e0b64a"/>
          <circle cx="100" cy="34" r="18" fill="#d4a93a"/>
          <rect x="130" y="20" width="86" height="30" rx="3" fill="#1f5a8c"/>
          <rect x="238" y="12" width="66" height="46" rx="3" fill="#1e3f7a"/>
          <circle cx="52" cy="118" r="38" fill="#2f4f8f"/>
          <circle cx="172" cy="116" r="38" fill="#2c2a5a"/>
          <circle cx="280" cy="116" r="30" fill="var(--white)" stroke="#2b5aa0" stroke-width="4"/>
        </svg>
      </div>
      <p class="tagline">Over 25 Years of Experience in Criminal Defense, DUI Defense and Personal Injury Cases. Serving all of Western PA.</p>
      <div class="office-photo" role="img" aria-label="Black and white photo of an attorney's desk with a nameplate"></div>
      <div class="consultation">
        <p class="label">FOR FREE CONSULTATION</p>
        <p class="phone"><small>CALL:</small> 412-555-0148</p>
        <p class="phone"><small>or</small>&nbsp; 412-555-0173</p>
        <p class="email">email: dan@drh-law.net</p>
        <p class="email">dhalvorsen@tobquill.net</p>
      </div>
    </div>
    <address class="mail-address">
      <span class="addressee">Daniel R. Halvorsen</span><br>
      1800 Barrister Tower<br>
      515 Grant Avenue<br>
      Pittsburgh, PA 15222<br>
      Pennsylvania, U.S.A
    </address>
    <div class="stamp-box">STAMP</div>
  </section>
</body>
</html>
```